Flyer for my live dj set from a recent party (party flyer included)

Need a recreation of a flyer for my live dj mix from the night of the party

(I added a pic of me and my logo if that looks good as well):

TEXT:

NO SITTING DOWN ON THE TILES HERE

VELLORIN STUDIOS One Year Anniversary Party 2019

QUILLA (Closing Set)

Recorded Live at Brasswick Hollow Brewery

pulsenest.example/quilla482

Target Market(s)

Electronic Music, Nightclub goers

Industry/Entity Type

Night Club

Font styles to use
Sans Serif

Colors

Designer to choose colors to be used in the design.

Requirements
Must have
• Elements of the original party flyer
Nice to have
• Some bright or neon, something that pops. Try to keep it similar to the flyer attached so it has the same theme and looks like a promo mix for that party

```html
<!DOCTYPE html>
<html lang="en">
<head>
<meta charset="utf-8">
<title>No Sitting Down on The Tiles Here — Quilla Closing Set</title>
<link rel="stylesheet" href="https://fonts.googleapis.com/css2?family=Abel&family=Open+Sans:wght@400&family=Rubik:wght@900&family=Gochi+Hand&family=Varela+Round&family=Permanent+Marker&display=block">
<style>
  :root {
    --bg: #05050a;
    --ink: #ffffff;
    --ink-soft: #d9d9de;
    --stage: #1d3034;
    --heart: #e3232c;
    --beam: rgba(255,255,255,0.10);
  }
  html, body {
    margin: 0;
    padding: 0;
    width: 1200px;
    height: 1200px;
    overflow: hidden;
    background: var(--bg);
  }
  .flyer {
    position: relative;
    width: 1200px;
    height: 1200px;
    overflow: hidden;
    background:
      radial-gradient(ellipse 560px 420px at 860px 600px, rgba(110,35,140,0.55), transparent 70%),
      radial-gradient(ellipse 700px 500px at 600px 520px, rgba(40,20,70,0.5), transparent 75%),
      var(--bg);
    color: var(--ink);
  }
  .beams {
    position: absolute;
    inset: 0;
  }
  .studio-name {
    position: absolute;
    top: 70px;
    left: 0;
    width: 100%;
    text-align: center;
    font-family: "Abel", sans-serif;
    font-size: 44px;
    line-height: 1;
    letter-spacing: 3px;
    color: var(--ink);
    margin: 0;
  }
  .headline {
    position: absolute;
    top: 196px;
    left: 0;
    width: 100%;
    text-align: center;
    font-family: "Abel", sans-serif;
    font-weight: 400;
    font-size: 76px;
    line-height: 1;
    white-space: nowrap;
    margin: 0;
    color: var(--ink);
  }
  .social {
    position: absolute;
    top: 304px;
    left: 0;
    width: 100%;
    text-align: center;
    font-family: "Open Sans", sans-serif;
    font-size: 22px;
    line-height: 1;
    color: var(--ink-soft);
    margin: 0;
  }
  .dj-photo {
    position: absolute;
    left: 496px;
    top: 344px;
    width: 704px;
    height: 600px;
    background:
      radial-gradient(ellipse 240px 300px at 380px 250px, rgba(230,110,150,0.75), transparent 70%),
      radial-gradient(ellipse 420px 200px at 420px 520px, rgba(150,40,110,0.7), transparent 75%),
      linear-gradient(180deg, rgba(60,20,90,0) 0%, rgba(90,30,110,0.6) 60%, rgba(40,10,40,0.9) 100%);
    -webkit-mask-image: linear-gradient(90deg, transparent 0%, #000 30%);
    mask-image: linear-gradient(90deg, transparent 0%, #000 30%);
  }
  .artist {
    position: absolute;
    left: 344px;
    top: 468px;
    width: 384px;
    text-align: right;
    margin: 0;
  }
  .artist-name {
    display: block;
    font-family: "Rubik", sans-serif;
    font-weight: 900;
    font-size: 76px;
    line-height: 1;
    letter-spacing: 2px;
    color: var(--ink);
  }
  .artist-set {
    display: block;
    margin-top: 14px;
    font-family: "Gochi Hand", sans-serif;
    font-size: 40px;
    line-height: 1;
    color: var(--ink);
  }
  .venue {
    position: absolute;
    left: 68px;
    top: 792px;
    display: flex;
    align-items: center;
    gap: 18px;
  }
  .venue-badge {
    width: 84px;
    height: 84px;
    border-radius: 50%;
    background: var(--ink);
    flex: none;
  }
  .venue-text {
    font-family: "Varela Round", sans-serif;
    font-size: 26px;
    line-height: 1.25;
    color: var(--ink);
    margin: 0;
  }
  .stage-band {
    position: absolute;
    left: 0;
    top: 944px;
    width: 100%;
    height: 34px;
    background: linear-gradient(180deg, var(--stage), rgba(10,16,18,0.4));
  }
  .love-house {
    position: absolute;
    left: 0;
    top: 1004px;
    width: 100%;
    display: flex;
    justify-content: center;
    align-items: center;
    gap: 30px;
  }
  .love-house .letter-i {
    font-family: "Abel", sans-serif;
    font-size: 62px;
    line-height: 1;
    color: var(--ink);
  }
  .event-title {
    position: absolute;
    top: 1098px;
    left: 0;
    width: 100%;
    text-align: center;
    font-family: "Permanent Marker", cursive;
    font-size: 50px;
    line-height: 1;
    letter-spacing: 3px;
    white-space: nowrap;
    margin: 0;
    color: var(--ink);
  }
</style>
</head>
<body>
<main class="flyer">
  <svg class="beams" width="1200" height="1200" viewBox="0 0 1200 1200" aria-hidden="true">
    <defs>
      <filter id="beam-blur"><feGaussianBlur stdDeviation="6"/></filter>
    </defs>
    <g filter="url(#beam-blur)" stroke="var(--beam)" stroke-width="22" fill="none">
      <line x1="600" y1="-40" x2="10" y2="950"/>
      <line x1="600" y1="-40" x2="1190" y2="950"/>
    </g>
  </svg>

  <p class="studio-name">VELLORIN STUDIOS</p>
  <h1 class="headline">No Sitting Down on The Tiles Here</h1>
  <p class="social">pulsenest.example/quilla482</p>

  <div class="dj-photo" role="img" aria-label="Photo of the DJ Quilla mixing on turntables under pink and purple club lights"></div>

  <h2 class="artist">
    <span class="artist-name">QUILLA</span>
    <span class="artist-set">( closing set )</span>
  </h2>

  <div class="venue">
    <div class="venue-badge"></div>
    <p class="venue-text">Recorded Live at<br>Brasswick Hollow Brewery</p>
  </div>

  <div class="stage-band"></div>

  <div class="love-house" aria-label="I love house music">
    <span class="letter-i">I</span>
    <svg width="62" height="56" viewBox="0 0 62 56" aria-hidden="true">
      <path d="M31 52 L6 27 A13 13 0 0 1 31 10 A13 13 0 0 1 56 27 Z" fill="none" stroke="var(--heart)" stroke-width="4" stroke-linejoin="round"/>
    </svg>
    <svg width="62" height="56" viewBox="0 0 62 56" aria-hidden="true">
      <path d="M4 28 L31 4 L58 28 M12 22 V52 H50 V22 M22 34 H40" fill="none" stroke="var(--ink)" stroke-width="4" stroke-linejoin="round"/>
    </svg>
    <svg width="50" height="58" viewBox="0 0 50 58" aria-hidden="true">
      <path d="M14 46 V8 L42 4 V40" fill="none" stroke="var(--ink)" stroke-width="4"/>
      <path d="M14 14 L42 10" stroke="var(--ink)" stroke-width="4"/>
      <ellipse cx="9" cy="47" rx="8" ry="6" fill="var(--ink)"/>
      <ellipse cx="37" cy="41" rx="8" ry="6" fill="var(--ink)"/>
    </svg>
  </div>

  <p class="event-title">ONE YEAR ANNIVERSARY PARTY 2019</p>
</main>
</body>
</html>
```